Brisk Hollow Builders Needs A Flyer

We need a flyer for our newest product "The Cedarlane Garden Workroom"

Here is some copy for the flyer:

1. More and more people everyday are working from home and finding it difficult to disconnect from home activities in order to focus on their work. They are also finding it very expensive to add on to their existing house for a quiet place. Our archatectually stunning, Cedarlane Garden Workroom is the answer. The office studio measures 16' wide and 10' deep. 160 Square feet of space.

Perfect for dozens of purposes. Home office, design studio, artist studio, home school office, reading room, craft studio, drafting room.

Features include:

- Steel Framing. 40-60% lighter then wood, higher strength to weight ratio, resistant to mold and fire and steel is the most recycled material on earth!
- Spray foam insulation. Cool in the summer and warm in the winter.
- HVAC Mini Split with wireless remote control and thermostat.
- 100% Off grid with enough solar and battery storage to run your entire office. No need to pay for an expensive electric installation.
- Flush fitting floor outlets to reduce wires.
- TV mount (Optional with pre-wired electric, HDMI, digital audio & Cat 6)
- Windows are tempered glass custom made by Morvik Glazing.
- Solar qualifies for a 26% tax credit. This is not a write-off rather it is a direct reduction on your tax obligation.
- Thousands of dollars less than adding onto your home.
- Custom color, siding, features available.

This beautiful back yard office is delivered 100% assembled and ready to enjoy on the day of delivery.

We ship nationwide from our factory in South Carolina. Give us a call anytime to speak to a designer and start your dream office today!

555-318-4027
info@BriskHollowBuilders.example

```html
<!DOCTYPE html>
<html lang="en">
<head>
<meta charset="utf-8">
<title>Brisk Hollow Builders – Cedarlane Garden Workroom Flyer</title>
<link href="https://fonts.googleapis.com/css2?family=Montserrat:wght@400;500;600;700;800&family=Oswald:wght@500&display=swap" rel="stylesheet">
<style>
  :root{
    --page-bg:#4a4845;
    --paper:#ffffff;
    --ink:#333333;
    --ink-soft:#555555;
    --gray-burst:#e9e9e9;
    --pill-dark:#3a3a3a;
    --orange:#f2a81d;
    --green:#3aa336;
    --green-dark:#2e8a2b;
  }
  *{box-sizing:border-box;margin:0;padding:0}
  html,body{width:1200px;height:730px;overflow:hidden}
  body{background:var(--page-bg);font-family:"Montserrat",sans-serif;color:var(--ink);display:flex;align-items:center;justify-content:center}
  .flyer{position:relative;width:544px;height:700px;background:var(--paper);overflow:hidden;box-shadow:0 6px 24px rgba(0,0,0,.35)}
  .flyer__backdrop{position:absolute;inset:0;width:100%;height:100%}
  .brand{position:absolute;left:32px;top:58px;width:168px;display:flex;align-items:center;gap:8px}
  .brand__dot{width:16px;height:16px;border-radius:50%;background:var(--green);flex:none}
  .brand__name{font-weight:700;font-size:17px;line-height:1.1;color:var(--green-dark)}
  .product-pill{position:absolute;left:32px;top:140px;width:166px;height:46px;border-radius:23px;background:var(--pill-dark);color:#fff;text-align:center;padding-top:7px;box-shadow:0 2px 4px rgba(0,0,0,.3)}
  .product-pill__name{display:block;font-weight:700;font-size:13.5px;line-height:1.15}
  .product-pill__sub{display:block;font-weight:500;font-size:11.5px}
  .dimensions{position:absolute;left:32px;top:205px;width:166px;text-align:center;font-size:11px;line-height:1.35;color:var(--ink)}
  .hero-art{position:absolute;left:212px;top:42px;width:318px;height:170px;border-radius:4px;background:linear-gradient(160deg,#5a5a5a 0%,#3b3b3b 35%,#d9cbb6 55%,#b9a58a 75%,#404040 100%)}
  .delivered{position:absolute;left:322px;top:257px;width:190px;text-align:center;font-size:7.5px;letter-spacing:1.6px;color:#666}
  .photo{position:absolute;left:325px;width:185px;border:4px solid #fff;box-shadow:0 1px 4px rgba(0,0,0,.3)}
  .photo--side{top:272px;height:146px;background:linear-gradient(180deg,#8fb2d2 0%,#c7d9e4 30%,#5d6a4a 45%,#6a6a62 70%,#4f7a34 100%)}
  .photo--front{top:437px;height:146px;background:linear-gradient(180deg,#a8c3d8 0%,#c8d8df 25%,#3d3d3d 40%,#c7b08f 65%,#4e7d33 100%)}
  .intro{position:absolute;left:32px;top:290px;width:260px}
  .intro__head{font-weight:600;font-size:13.5px;line-height:1.2;color:var(--ink)}
  .intro__body{margin-top:6px;font-size:7px;line-height:1.45;color:var(--ink-soft)}
  .features-tag{position:absolute;left:32px;top:388px;padding:4px 10px;border:1.5px solid var(--orange);border-radius:12px;font-weight:700;font-size:11px;color:var(--ink)}
  .features{position:absolute;left:32px;top:420px;width:262px;list-style:none}
  .features li{position:relative;padding-left:16px;font-size:7.2px;line-height:1.4;color:var(--ink-soft);margin-bottom:4.6px}
  .features li b{color:var(--ink);font-weight:700}
  .features svg{position:absolute;left:0;top:2px;width:9px;height:8px}
  .contact{position:absolute;left:322px;top:616px;width:190px;height:84px;background:var(--green);border-radius:22px 22px 0 0;color:#fff;text-align:center;padding-top:11px}
  .contact__phone{display:block;font-family:"Oswald",sans-serif;font-weight:500;font-size:30px;line-height:1.1}
  .contact__email{display:block;margin-top:6px;font-size:9px}
  .flyer__base{position:absolute;left:0;bottom:0;width:100%;height:5px;background:var(--green)}
</style>
</head>
<body>
<main class="flyer">
  <svg class="flyer__backdrop" viewBox="0 0 544 700" aria-hidden="true">
    <defs>
      <radialGradient id="burst" cx="0.3" cy="0.25" r="0.7">
        <stop offset="0" stop-color="#ffffff"/>
        <stop offset="1" stop-color="#dcdcdc"/>
      </radialGradient>
    </defs>
    <path d="M0 0H544V190C420 250 250 262 0 268Z" fill="url(#burst)"/>
    <path d="M0 268C250 262 420 250 544 190V202C420 262 250 274 0 282Z" fill="var(--orange)"/>
  </svg>

  <div class="brand">
    <span class="brand__dot"></span>
    <span class="brand__name">Brisk Hollow Builders</span>
  </div>

  <div class="product-pill">
    <span class="product-pill__name">Cedarlane Garden</span>
    <span class="product-pill__sub">Workroom</span>
  </div>

  <p class="dimensions">16' wide and 10' deep<br>160 Sqft. of space</p>

  <div class="hero-art" role="img" aria-label="Rendering of the dark-clad garden workroom with a slanted roof and glass doors"></div>

  <p class="delivered">DELIVERED 100% ASSEMBLED</p>

  <div class="photo photo--side" role="img" aria-label="Side view of the workroom with solar panels on the roof in a green yard"></div>
  <div class="photo photo--front" role="img" aria-label="Front view of the workroom with glass doors set in a garden"></div>

  <section class="intro">
    <h1 class="intro__head">More and more people<br>everyday are working from home</h1>
    <p class="intro__body">and finding it difficult to disconnect from home activities in order to focus on their work. They are also finding it very expensive to add on to their existing house for a quiet place.</p>
  </section>

  <h2 class="features-tag">FEATURES INCLUDE:</h2>

  <svg width="0" height="0" style="position:absolute">
    <symbol id="tick" viewBox="0 0 10 8"><path d="M1 4.2L3.8 7 9 1" fill="none" stroke="#3aa336" stroke-width="2" stroke-linecap="round" stroke-linejoin="round"/></symbol>
  </svg>
  <ul class="features">
    <li><svg><use href="#tick"/></svg><b>Steel Framing.</b> 40-60% lighter then wood, higher strength to weight ratio, resistant to mold and fire and steel is the most recycled material on earth!</li>
    <li><svg><use href="#tick"/></svg><b>Spray foam insulation.</b> Cool in the summer and warm in the winter.</li>
    <li><svg><use href="#tick"/></svg><b>HVAC Mini Split</b> with wireless remote control and thermostat.</li>
    <li><svg><use href="#tick"/></svg><b>100% Off grid</b> with enough solar and battery storage to run your entire office. No need to pay for an expensive electric installation.</li>
    <li><svg><use href="#tick"/></svg><b>Flush fitting floor outlets</b> to reduce wires.</li>
    <li><svg><use href="#tick"/></svg><b>TV mount</b> (Optional with pre-wired electric, HDMI, digital audio &amp; Cat 6)</li>
    <li><svg><use href="#tick"/></svg><b>Windows are tempered glass</b> custom made by Morvik Glazing.</li>
    <li><svg><use href="#tick"/></svg><b>Solar qualifies for a 26% tax credit.</b> This is not a write-off rather it is a direct reduction on your tax obligation.</li>
    <li><svg><use href="#tick"/></svg><b>Thousands of dollars less</b> than adding onto your home.</li>
    <li><svg><use href="#tick"/></svg><b>Custom</b> color, siding, features available.</li>
  </ul>

  <div class="contact">
    <span class="contact__phone">555-318-4027</span>
    <span class="contact__email">info@BriskHollowBuilders.example</span>
  </div>

  <div class="flyer__base"></div>
</main>
</body>
</html>
```